Bref créative
Stationary Package - Paper, Envelope, Fax Cover, Bus. Card
Mortgage Co. seeks Stationary Package
Professional
Marla Henson
Broker / Owner
246 W. "K" Avenue
Upland CA 91704
MarlaHenson@quillmail.example
DRE LIC 05837162 NMLS 489153
Head Shot Photo on Front about a 1/3 of the card to 1/4. Should have company name/logo on the front "KGV Lending Corp." or Corporation whichever looks better
MarlaHenson.example MarlaHensonRE.example KGVLending.example
Home Loans & Real Estate Investments,
Mortgage Broker, Licensed Real Estate Broker,
California Certified Residential Property Manager (CPM),
Short Sale & Foreclosure Resource Certified (SFR),
BS Business Admin., University of Brookhollow, CA

```html
<!DOCTYPE html>
<html lang="en">
<head>
<meta charset="utf-8">
<title>KGV Lending Corp. Stationery</title>
<link href="https://fonts.googleapis.com/css2?family=Source+Sans+3:wght@400;600;700&display=swap" rel="stylesheet">
<style>
  :root {
    --navy: #1b3f8f;
    --blue: #2a5cc0;
    --sky: #d6e0f0;
    --mist: #eef2f8;
    --ink: #1d1d1f;
    --grey: #5f646d;
    --paper: #ffffff;
    --edge: #c9ced8;
  }
  * { margin: 0; padding: 0; box-sizing: border-box; }
  html, body { width: 1200px; height: 718px; overflow: hidden; background: var(--paper); }
  body { position: relative; font-family: "Source Sans 3", Arial, sans-serif; color: var(--ink); }

  .sheet { position: absolute; border: 1px solid var(--edge); overflow: hidden; }
  .sheet::before { content: ""; position: absolute; left: 0; right: 0; top: 0; height: 4px; background: var(--blue); }

  .letterhead { left: 5px; top: 2px; width: 555px; height: 714px; background: linear-gradient(180deg, var(--paper) 0%, var(--paper) 50%, var(--sky) 100%); }
  .fax-sheet { left: 578px; top: 2px; width: 617px; height: 268px; background: linear-gradient(180deg, var(--paper) 0%, var(--paper) 35%, var(--sky) 100%); }
  .fax-sheet::after { content: ""; position: absolute; left: 0; right: 0; bottom: 0; height: 4px; background: var(--blue); }

  .brand { position: absolute; display: flex; align-items: center; gap: 10px; }
  .brand-mark { width: 22px; height: 22px; border-radius: 50%; background: var(--navy); flex: none; }
  .brand-name { font-weight: 700; color: var(--navy); line-height: 1; white-space: nowrap; }
  .letterhead .brand { left: 36px; top: 86px; }
  .letterhead .brand-name { font-size: 32px; }
  .fax-sheet .brand { left: 40px; top: 42px; }
  .fax-sheet .brand-name { font-size: 24px; }
  .fax-sheet .brand-mark { width: 18px; height: 18px; }

  .license { position: absolute; font-size: 12px; font-weight: 600; color: var(--blue); white-space: nowrap; }
  .letterhead .license { left: 36px; top: 130px; }
  .fax-sheet .license { left: 40px; top: 76px; font-size: 10px; }

  .signer { position: absolute; right: 28px; top: 96px; text-align: right; }
  .signer-name { font-size: 19px; font-weight: 700; color: var(--navy); line-height: 1.2; }
  .signer-role { font-size: 12px; color: var(--ink); }

  .faint-brand { position: absolute; color: var(--navy); opacity: .07; font-weight: 700; line-height: 1; }
  .letterhead .faint-brand { left: 130px; top: 520px; font-size: 110px; }
  .fax-sheet .faint-brand { left: 390px; top: 90px; font-size: 76px; }

  .address { position: absolute; left: 0; right: 0; text-align: center; font-weight: 700; white-space: nowrap; }
  .letterhead .address { top: 670px; font-size: 15px; }
  .fax-sheet .address { top: 224px; font-size: 12px; }

  .contact-bar { position: absolute; left: 0; right: 0; display: flex; justify-content: center; gap: 12px; font-size: 9px; white-space: nowrap; }
  .contact-bar b { font-weight: 700; margin-right: 10px; }
  .contact-bar .sep { color: var(--grey); }
  .letterhead .contact-bar { top: 696px; }
  .fax-sheet .contact-bar { top: 244px; font-size: 8px; gap: 10px; }

  .envelope { position: absolute; left: 578px; top: 278px; width: 617px; height: 438px; border: 1px solid var(--edge); background: linear-gradient(180deg, var(--paper) 30%, var(--mist) 75%, var(--sky) 100%); overflow: hidden; }
  .envelope-flap { position: absolute; left: 0; top: 0; width: 617px; height: 64px; }
  .envelope .brand { left: 50%; top: 18px; transform: translateX(-50%); gap: 8px; }
  .envelope .brand-name { color: var(--paper); font-size: 18px; }
  .envelope .brand-mark { width: 14px; height: 14px; background: var(--paper); }
</style>
</head>
<body>

<section class="sheet letterhead">
  <div class="brand"><span class="brand-mark"></span><span class="brand-name">KGV Lending Corp.</span></div>
  <p class="license">DRE LIC 05837162 NMLS 489153</p>
  <div class="signer">
    <p class="signer-name">Marla Henson</p>
    <p class="signer-role">Broker / Owner</p>
  </div>
  <p class="faint-brand" aria-hidden="true">KGV</p>
  <p class="address">246 W. "K" Avenue, Upland CA 91704</p>
  <p class="contact-bar">
    <span><b>Phone</b>555-014-2870</span><span class="sep">|</span>
    <span><b>Cell</b>555-016-4417</span><span class="sep">|</span>
    <span><b>Fax</b>555-014-2871</span><span class="sep">|</span>
    <span><b>Email</b>MarlaHenson@quillmail.example</span>
  </p>
</section>

<section class="sheet fax-sheet">
  <div class="brand"><span class="brand-mark"></span><span class="brand-name">KGV Lending Corp.</span></div>
  <p class="license">DRE LIC 05837162 NMLS 489153</p>
  <p class="faint-brand" aria-hidden="true">KGV</p>
  <p class="address">246 W. "K" Avenue, Upland CA 91704</p>
  <p class="contact-bar">
    <span><b>Phone</b>555-014-2870</span><span class="sep">|</span>
    <span><b>Cell</b>555-016-4417</span><span class="sep">|</span>
    <span><b>Fax</b>555-014-2871</span><span class="sep">|</span>
    <span><b>Email</b>MarlaHenson@quillmail.example</span>
  </p>
</section>

<section class="envelope">
  <svg class="envelope-flap" viewBox="0 0 617 64" aria-hidden="true">
    <defs>
      <linearGradient id="flapBlue" x1="0" y1="0" x2="1" y2="0">
        <stop offset="0" stop-color="#1b3f8f"/>
        <stop offset=".5" stop-color="#2f6ad0"/>
        <stop offset="1" stop-color="#1b3f8f"/>
      </linearGradient>
    </defs>
    <polygon points="0,0 617,0 598,48 308,64 19,48" fill="url(#flapBlue)"/>
  </svg>
  <div class="brand"><span class="brand-mark"></span><span class="brand-name">KGV</span></div>
</section>

</body>
</html>
```